VORNEK Unmanned Aircraft Systems needs a Company Brochure design

We need a company brochure for UAV manufacturer that contains a detailed company brief of our mission, vision, company ethos, product range, etc.

The Brochure should be in a A4 size with about a range of about 10-15 pages (there can be more if all information does not fit). The final document will have to be in PDF format to be shared with clients. A digital PDF version is preferred, this will not necessarily be printed as we share most documents online,

Our company colors are #FF8000 & #6e6e6e, however, we would like to keep the design clean, simple, visually appealing, and minimalistic (see the example attached). We would like a simial look & feel to this.

We do not want to over saturate pages with information and want to keep it as visual as possible by using infographics, images, and icons. We would like this brochure to provide clients with information on what we do, our mission, vision, ethos, how we have grown, industries we serve, aircraft we offer, consulting & training services, and also showcase our current clients & partners.

We would also like to see information on the different payloads offered (reference in VORNEK Brcihure V2). We would also like to get the look & feel created on the QR7 brochure in terms of the background being clear but showcasing elements of the aircraft.

Please refer to the website: www.vornekuas.example for more information on VORNEK.

Who is VORNEK:
VORNEK is an award-winning unmanned manufacturing company, based in Knysna, South Africa, with a focus on long-endurance vertical take-off and landing unmanned aircraft. VORNEK was born out of the need to increase endurance while retaining the ability to operate from very confined areas without the need for a runway for take-off and landings. A brand-new vehicle had to be developed from the ground up and thus the VORNEK Meridian was created and started shipping out in early 2017.

Our team has nearly a decade of manufacturing, 3D printing, rapid prototyping and sales experience, in-house engineering as well as software development. We are currently the largest commercial drone manufacturer in Africa and the current world leader of small unmanned VTOL fixed-wing aircraft.

What we do:
We design, manufacture, source, and supply industry-leading unmanned aircraft systems for the most demanding operations around the world. Expert, experienced consulting and technical guidance, sales, training, support, and beyond.

VORNEK has 10+ years of Unmanned Aircraft experience, allowing us to provide a high level of expertise and skill, and have been shipping aircraft worldwide since 2012. Our aircraft are currently in 13+ Countries (This would be nice to be displayed on a map of where our aircraft are).

We provide both consulting and a wide range of unmanned aircraft which range from a 2m to a 6m wingspan. Our range of VTOL hybrid aircraft are the K5, T8, Meridian, J71, T9, Summit, T2, and our range of multirotor includes the G4 & H6.

Our Mission:
VORNEK offers a single point of contact for anything and everything VTOL, along with a comprehensive selection of multi-rotor, fixed-wing, and hybrid solutions, payloads, and communication.

Why fly VORNEK? (We would like this section to be illustrated with graphics)
Low Running Cost: Fly further for longer at a low operating cost of only $3 an hour
High Endurance: Collect all data in a single flight with endurance of up to 10+ hours
Cover More Ground: Cover more ground with an operating link range of up to 150 km
Rapidly Deploy: Set-up deployed from in the case to in the air in under 10 minutes
Capture Accurate Data: Real-time HD video & data streamed to C2, control rooms & across networks
Multi-payload Capability: Designed to fly advanced duel sensor stabilized day & night EO/IR payloads
Take-off & land anywhere: Runway independent with no need for bulky launch or recovery equipment
Autonomous flight: Peace-of-mind operation & safe flight control from take-off to landing
Maximize efficiency: Save valuable time, assets, and resources with reduced human risk

What is VTOL:
'Vertical Take-off and Landing' - The ability for an unmanned aircraft to launch without the need for a runway or other bulky and costly hardware, rapidly and reliably.

VORNEK unmanned aircraft use a reliable battery-powered quad-copter component for vertical take-off and landing, paired with an efficient fuel-powered combustion engine for forward flight. After start-up, the aircraft vertically ascends to altitude, where it transitions into forward fixed-wing bound flight for the duration of the mission. Once completed, the aircraft performs a smooth & level back transition into a solid hover allowing it to land vertically.

Industries we serve (For this section please also make use of graphics to showcase the benefits of each application, refer to how it has been done in the QR7 brochure). From civil to military, commercial to industrial.

Police & law enforcement - UAVs allow for quicker action, more accurate results, and uninterrupted real-time aerial
surveillance. Benefits include:
- Longer flight times and more coverage
- Aerial surveillance & GEO Lock
- Rapidly deploy the VORNEK VTOL in an urban environment
- Situational planning & assessment

Surveillance & Reconnaissance - With UAVs security teams can make quick, strategic decisions in life-threatening
situations. Benefits include:
- Real-time aerial surveillance
- Improved data accuracy
- Flexibility, availability & accessibility
- Improved efficiency

Coast Guard & Maritime - Fast deployment and response time is critical. UAVs allow you to detect small targets while surveying and includes benefits like:
- Real-time situational awareness
- Remote operation
- Minimize risk and human interaction
- Rapid response

Conservation - UAVs allow for closer monitoring, assessment, and observation of animals and nature. Other benefits include:
- Autonomous flight
- Remote monitoring with minimal human interference
- Species management & behavior tracking
- Rule enforcement

Border control - VORNEK UAVs allow operators to get a continuous & clear aerial view of the border. Maximize
border control with benefits like:
- Large area coverage
- Extended range
- Reduced labor costs
- Real-time imaging

Wildfire Management - Benefits of UAV use in wildfire management include:
- Real-time situational awareness to track the spread and movement of fires
- Damage assessment
- Severity analysis
- Back burning prevention

Mining - Mining is known to be one of the most
dangerous and asset-heavy industries in the world. UAV mining benefits include:
- Monitoring, Inspection & Exploration
- Stockpile management
- Perimeter security
- Automatic surveying

Search & Rescue - The use of UAVs in search and rescue allows first responders to quickly assess the severity of a situation. Other benefits include:
- Aerial surveillance
- Emergency response
- Target locating
- Increased situation awareness

Aircraft (For this section make use of the description as well as the key features for each as listed - images of each will be uploaded shortly)
K5: The VORNEK K5 is our most compact fixed-wing VTOL unmanned aircraft in the fleet with a wingspan of only 2 meters. This all-electric system has been developed for tight launch and landing zones, can be used for multiple applications from search and rescue, surveillance to infrastructure inspection, and is capable of carrying a wide variety of payloads of up to 0.8 kg. The VORNEK K5 offers excellent situational awareness with an endurance of up to 1.5 hours in a single flight allowing for rapid deployment in multiple mission scenarios.
Key Features - 2m Wingspan, 0.8 kg Payload, Up to 1.5h Endurance, 15km Range

T8: The VORNEK T8 VTOL system is the ideal low-cost aircraft for surveillance and reconnaissance missions that require rapid deployment in remote areas without the need for a runway or recovery equipment. Due to its advanced avionics, the T8 can be programmed to complete fully autonomous missions from take-off to landing and stay in the air for up to 3 hours, allowing operators to cover far more ground quicker. When paired with an advanced stabilized EO/IR payload the T8 can be operated in both day and night surveillance missions.
Key Features - 3m Wingspan, 2 kg Payload, 3h Endurance. 50km Range

Meridian: The VORNEK Meridian delivers up to 8 hours of endurance and a range of 600 km in a single flight. Runway independent and rapidly deployed, the Meridian can be set up from in the case to in the air in under 10 minutes. With the capacity to carry advanced dual sensor stabilized day and night EO/IR payloads of up to 1 kg, the Meridian is ideally suited for border patrol, search & rescue, and other long-range applications. The VORNEK Meridian also features our all-in-one purpose-built VORNEK Nublex autopilot and power distribution system and ground control system.
Key Features - 3m Wingspan, 1 kg Payload, 8h Endurance. 50km Range

J71: The VORNEK J71 is a 4 meter all-electric VTOL with a flight endurance of up to 3 hours and the ability to carry a wide variety of advanced EO/IR payload sensors of up to 3 kg while maintaining high endurance figures and reliability. Not only do the VTOL capabilities of the J71 allow for additional reliability and safety, but it is also equipped with a long-range data link, allowing operators to fly further and capture more data.
Key Features - 3m Wingspan, 3 kg Payload, 3h Endurance. 50km Range

T9: The VORNEK T9 features a longer wingspan to the T8, allowing for longer endurance and heavier payloads, paired with a high-end EFI combustion engine, the T9 is ideal for serious surveillance work. The modular airframe allows users to set up and deploy the UAV quickly and effectively without the need for a runway, launch, or recovery equipment. This 4-meter aircraft is able to fly for up to 4 hours while carrying an advanced EO/IR payload of up to 3 kg in a single flight and is equipped with a long-range ground control station that delivers between 10 to 100 km. The VORNEK T9 is optimized for efficient, reliable, and safe VTOL operations.
Key Features - 4m Wingspan, 3 kg Payload, 4h Endurance. 100km Range

Summit: Our Flagship, the VORNEK Summit. Offering a higher payload capacity of up to 5kg and 10 hours of flight endurance, top-of-the-range equipment, payloads, and communication systems, the Summit is the ultimate in VTOL technology. Allowing our clients to cover more ground and gain access to hard-to-reach places and data. The advanced aerodynamic design allows for excellent stability in high winds and efficient cruise with ultra-low drag. The Summit also features quick-lock & latch connectors that enable rapid deployment from case to in the air in under 20 minutes. The Summit offers a longer range than any of our other aircraft and can fly a wide variety of different payloads, sensors, communication options, and more to suit the highest mission requirements.
Key Features - 5m Wingspan, 5 kg Payload, 10+h Endurance. 150km Range

T2: Boasting endurance of up to 10 hours, alongside our industry-leading range of up to 150 km. When paired with an advanced payload of up to 5 kg this aircraft is the ideal solution to minimizing risk during critical missions. The T2 is also a VTOL hybrid, making it completely runway independent with a small operational footprint, offering rapid deployment. In addition, the T2 features an advanced autopilot and ground control system.
Key Features - 6m Wingspan, 5 kg Payload, 10h Endurance. 150km Range

VORNEK Z4 Command & Control
The VORNEK Z4 Command & Control station is a reliable, long-range ground control system developed specifically for quick mission planning, easy flight control, and custom integration capabilities of any VORNEK aircraft in the fleet. The C2 allows operators to switch seamlessly between different flight modes and payload settings while streaming real-time data telemetry and video communication from the aircraft while in flight. The VORNEK Z4 comes in a rugged, compact, and portable ravine HULL case and features two (2) large HD monitors, relevant pre-loaded mission planning & payload software, data telemetry, a combination of advanced data links, such as the Korvath Beamrunner, and hot-swappable battery packs for uninterrupted and continuous operation in the field.
What is included:
VORNEK GCS with Ravine Case
Radio Controller & Umbilical Cable
Keyboard & Mouse
Desktop Power Supply & Holder
Batteries & Battery Bay
Data-link & Control Antennas
Payload Controller

Autopilot - VORNEK Nublex
The Nublex is an ultra-compact, affordable, reliable, and easy-to-use solution designed and manufactured in-house by VORNEK. It supports an extensive range of configurations, power requirements, and systems including but not limited to fixed-wing, multi-rotor, and VTOL unmanned aircraft. The Nublex comes with an advanced control system built-in – making installation and setup quicker, easier, and more convenient. The built-in industry-leading long-range control system is supplemented with:
Active cooling and temperature control
A vibration isolation mount
Ultra-reliable, high-quality connectors
Redundant & adjustable power supplies
An advanced microprocessor
Navigation lighting system
14 Channel output

All these features come enclosed in a rugged, durable and lightweight casing that is built to last.

Supported flight modes include:
Start-up (Manual)
Q-Hover
Cruise
Return to Launch (RTL)
Auto/Mission
Hold
Guided Mode
Q-Stabilize
The world’s first and only complete all-in-one Avionics system for fixed-wing VTOL unmanned aircraft.

VORNEK Autopilot Fail-safes:
Q Assist Speed - VTOL motors assist when airspeed is lower than Q Assist Speed (17m/s)
Q Assist Angle - VTOL motors assist when the roll angle is higher than 40∘
Stall Detection - Q Assist mode will automatically enable to maintain of a safe flight envelope
Max Altitude Limits Exceed - Aircraft will descend to a safe altitude
Airspeed Sensor Failure - Automatic detection & warning, will continue normal flight with IMU

Payload Options (This section only has to display the different payload options offered with little detail)
Sparrowin
Sparrowin 348
Duskowlet 2
Duskowlet 2 UZ
Kestrelo
QM31
QM57-LV
QM57-LV-CZ-GS
QM92

Please also add a place to showcase client logo's (these have been added to resources and can also be seen on the website)

Refer to the VORNEK Brochure V2 for more information that can be used and to the QR7 for design look & feel.
The aircraft spec sheet has been uploaded as a reference of the type of designs we like, but full specs will only be added once a final design has been selected as this information is confidential

Target Market(s)

Military & Security Firms

Industry/Entity Type

Aerospace & Aviation

Font styles to use
Other font styles liked:
• Raleway

Colors

Designer to choose colors to be used in the design.

Requirements
Must have
• Infographics, Icons, Bold Elements
Nice to have
• We would like to use the aircraft as a background while keeping a white background (so not the m=image just elements of the image)

```html
<!DOCTYPE html>
<html lang="en">
<head>
<meta charset="utf-8">
<title>VORNEK Brochure – Aircraft Spread</title>
<link href="https://fonts.googleapis.com/css2?family=Raleway:wght@300;400;500&display=swap" rel="stylesheet">
<style>
:root{
  --bg:#d8894e;
  --orange:#f07f1a;
  --grey-text:#6e6e6e;
  --rule:#b5b5b5;
  --page-white:#ffffff;
  --page-grey:#d9d9d9;
  --tile:#e6e6e6;
  --tile-dark:#d2d2d2;
}
*{margin:0;padding:0;box-sizing:border-box}
html,body{width:1200px;height:824px;overflow:hidden;background:var(--bg)}
body{font-family:'Raleway',sans-serif;color:var(--grey-text)}
.spread{position:absolute;left:37px;top:13px;width:1372px;height:972px;transform:scale(0.82);transform-origin:0 0}
.page{position:absolute;top:0;height:972px;width:686px}
.page--left{left:0;background:linear-gradient(90deg,var(--page-white) 0%,var(--page-white) 40%,var(--page-grey) 100%)}
.page--right{left:686px;background:linear-gradient(90deg,#d4d4d4 0%,#e6e6e6 40%,#efefef 100%)}
.folio{position:absolute;top:32px;font-size:8px;font-weight:400;display:flex;align-items:baseline;gap:10px;color:#555}
.folio__num{font-size:15px;font-weight:300}
.section-tag{position:absolute;top:88px;width:112px;height:30px;background:var(--orange);color:#fff;font-size:17px;font-weight:300;padding:5px 12px}
.tile{position:absolute;width:148px;height:148px;background:radial-gradient(circle at 50% 50%,var(--tile-dark) 0%,var(--tile) 70%)}
.hero{position:absolute;left:454px;top:80px;width:150px;height:75px;background:radial-gradient(ellipse at 50% 50%,#c4c6cc 0%,rgba(220,220,220,0) 70%)}
.product{position:absolute}
.product__title{font-size:17px;font-weight:300;color:var(--orange);line-height:1}
.product__rule{width:30px;height:2px;background:var(--rule);margin:10px 0 14px}
.product__body{font-size:8.6px;line-height:11.1px;font-weight:400;text-align:justify}
.product__features{font-size:8.6px;line-height:11.1px;margin-top:10px;text-align:justify}
.product__features span{color:var(--orange)}
</style>
</head>
<body>
<div class="spread">
  <section class="page page--left">
    <div class="folio" style="left:52px"><span class="folio__num">8</span><span>© 2021 VORNEK UAS (PTY) LTD</span></div>
    <div class="section-tag" style="left:48px">Aircraft</div>

    <div class="tile" style="left:48px;top:151px" role="img" aria-label="Top-view silhouette of the K5 aircraft"></div>
    <article class="product" style="left:235px;top:150px;width:260px">
      <h2 class="product__title">K5</h2>
      <div class="product__rule"></div>
      <p class="product__body">The VORNEK K5 is our most compact fixed-wing VTOL unmanned aircraft in the fleet with a wingspan of only 2 meters. This all-electric system has been developed for tight launch and landing zones, can be used for multiple applications from search and rescue, surveillance to infrastructure inspection, and is capable of carrying a wide variety of payloads of up to 0.8 kg. The VORNEK K5 offers excellent situational awareness with an endurance of up to 1.5 hours in a single flight allowing for rapid deployment in multiple mission scenarios.</p>
      <p class="product__features"><span>Key Features</span> - 2m Wingspan, 0.8 kg Payload, Up to 1.5h Endurance, 15km Range</p>
    </article>

    <div class="tile" style="left:48px;top:355px" role="img" aria-label="Top-view silhouette of the T8 aircraft"></div>
    <div class="tile" style="left:323px;top:355px" role="img" aria-label="Top-view silhouette of the Meridian aircraft"></div>

    <article class="product" style="left:57px;top:522px;width:235px">
      <h2 class="product__title">T8</h2>
      <div class="product__rule"></div>
      <p class="product__body">The VORNEK T8 VTOL system is the ideal low-cost aircraft for surveillance and reconnaissance missions that require rapid deployment in remote areas without the need for a runway or recovery equipment. Due to its advanced avionics, the T8 can be programmed to complete fully autonomous missions from take-off to landing and stay in the air for up to 3 hours, allowing operators to cover far more ground quicker. When paired with an advanced stabilized EO/IR payload the T8 can be operated in both day and night surveillance missions.</p>
      <p class="product__features"><span>Key Features</span> - 3m Wingspan, 2 kg Payload, 3h Endurance. 50km Range</p>
    </article>

    <article class="product" style="left:323px;top:522px;width:234px">
      <h2 class="product__title">Meridian</h2>
      <div class="product__rule"></div>
      <p class="product__body">The VORNEK Meridian delivers up to 8 hours of endurance and a range of 600 km in a single flight. Runway independent and rapidly deployed, the Meridian can be set up from in the case to in the air in under 10 minutes. With the capacity to carry advanced dual sensor stabilized day and night EO/IR payloads of up to 1 kg, the Meridian is ideally suited for border patrol, search &amp; rescue, and other long-range applications. The VORNEK Meridian also features our all-in-one purpose-built VORNEK Nublex autopilot and power distribution system and ground control system.</p>
      <p class="product__features"><span>Key Features</span> - 3m Wingspan, 1 kg Payload, 8h Endurance. 50km Range</p>
    </article>
  </section>

  <section class="page page--right">
    <div class="folio" style="right:52px"><span>© 2021 VORNEK UAS (PTY) LTD</span><span class="folio__num">9</span></div>
    <div class="section-tag" style="left:47px">Aircraft</div>
    <div class="hero" role="img" aria-label="Rendered VTOL aircraft in flight"></div>

    <div class="tile" style="left:47px;top:151px" role="img" aria-label="Top-view silhouette of the J71 aircraft"></div>
    <article class="product" style="left:215px;top:159px;width:389px">
      <h2 class="product__title">J71</h2>
      <div class="product__rule"></div>
      <p class="product__body">The VORNEK J71 is a 4 meter all-electric VTOL with a flight endurance of up to 3 hours and the ability to carry a wide variety of advanced EO/IR payload sensors of up to 3 kg while maintaining high endurance figures and reliability. Not only do the VTOL capabilities of the J71 allow for additional reliability and safety, but it is also equipped with a long-range data link, allowing operators to fly further and capture more data.</p>
      <p class="product__features"><span>Key Features</span> - 3m Wingspan, 3 kg Payload, 3h Endurance. 50km Range</p>
    </article>

    <div class="tile" style="left:47px;top:355px" role="img" aria-label="Top-view silhouette of the T9 aircraft"></div>
    <div class="tile" style="left:349px;top:355px;background:radial-gradient(circle,#c8c8c8 0%,#d6d6d6 70%)" role="img" aria-label="Top-view silhouette of the Summit aircraft"></div>

    <article class="product" style="left:47px;top:522px;width:271px">
      <h2 class="product__title">T9</h2>
      <div class="product__rule"></div>
      <p class="product__body">The VORNEK T9 features a longer wingspan to the T8, allowing for longer endurance and heavier payloads, paired with a high-end EFI combustion engine, the T9 is ideal for serious surveillance work. The modular airframe allows users to set up and deploy the UAV quickly and effectively without the need for a runway, launch, or recovery equipment. This 4-meter aircraft is able to fly for up to 4 hours while carrying an advanced EO/IR payload of up to 3 kg in a single flight and is equipped with a long-range ground control station that delivers between 10 to 100 km. The VORNEK T9 is optimized for efficient, reliable, and safe VTOL operations.</p>
      <p class="product__features"><span>Key Features</span> - 4m Wingspan, 3 kg Payload, 4h Endurance. 100km Range</p>
    </article>

    <article class="product" style="left:352px;top:522px;width:270px">
      <h2 class="product__title">Summit</h2>
      <div class="product__rule"></div>
      <p class="product__body">Our Flagship, the VORNEK Summit. Offering a higher payload capacity of up to 5kg and 10 hours of flight endurance, top-of-the-range equipment, payloads, and communication systems, the Summit is the ultimate in VTOL technology. Allowing our clients to cover more ground and gain access to hard-to-reach places and data. The advanced aerodynamic design allows for excellent stability in high winds and efficient cruise with ultra-low drag. The Summit also features quick-lock &amp; latch connectors that enable rapid deployment from case to in the air in under 20 minutes. The Summit offers a longer range than any of our other aircraft and can fly a wide variety of different payloads, sensors, communication options, and more to suit the highest mission requirements.</p>
      <p class="product__features"><span>Key Features</span> - 5m Wingspan, 5 kg Payload, 10+h Endurance. 150km Range</p>
    </article>

    <div class="tile" style="left:47px;top:758px" role="img" aria-label="Top-view silhouette of the T2 aircraft"></div>
    <article class="product" style="left:215px;top:766px;width:389px">
      <h2 class="product__title">T2</h2>
      <div class="product__rule"></div>
      <p class="product__body">Boasting endurance of up to 10 hours, alongside our industry-leading range of up to 150 km. When paired with an advanced payload of up to 5 kg this aircraft is the ideal solution to minimizing risk during critical missions. The T2 is also a VTOL hybrid, making it completely runway independent with a small operational footprint, offering rapid deployment. In addition, the T2 features an advanced autopilot and ground control system.</p>
      <p class="product__features"><span>Key Features</span> - 6m Wingspan, 5 kg Payload, 10h Endurance. 150km Range</p>
    </article>
  </section>
</div>
</body>
</html>
```